Marlows Pet Care

Hi. I need a business card /logo for my pet care business. Im thinking about a dogs paw print. Although i do look after other pets so don't want to restrict my self. Open to suggestions on colour etc but like greens and purples.The name of my business is marlow's pet care. The logo could be just an image or have marlows power care on it. An option to do either would be great. For the winner i also would like a Web page (word press template if possible) designed if you can, of course I'll pay additional for this. Look forward to your ideas!

```html
<!DOCTYPE html>
<html lang="en">
<head>
<meta charset="utf-8">
<title>Marlow's Pet Care — Business Card</title>
<link href="https://fonts.googleapis.com/css2?family=Open+Sans:wght@400;600;700&display=swap" rel="stylesheet">
<style>
  :root {
    --purple: #743a94;
    --green: #a6e00f;
    --white: #ffffff;
    --paper: #f4f4f4;
    --backdrop: #e6e6e6;
    --shadow: rgba(0, 0, 0, 0.18);
  }
  * { margin: 0; padding: 0; box-sizing: border-box; }
  html, body {
    width: 1200px;
    height: 900px;
    overflow: hidden;
  }
  body {
    background: radial-gradient(circle at 50% 45%, #f3f3f3 0%, var(--backdrop) 75%);
    font-family: "Open Sans", Arial, sans-serif;
    position: relative;
  }
  .card {
    position: absolute;
    left: 250px;
    width: 700px;
    height: 400px;
    border-radius: 4px;
    overflow: hidden;
    box-shadow: 0 14px 30px var(--shadow);
  }
  .card--front { top: 30px; background: linear-gradient(135deg, var(--white), var(--paper)); }
  .card--back { top: 470px; background: var(--purple); }

  .card__shapes { position: absolute; inset: 0; width: 100%; height: 100%; }

  .brand {
    position: absolute;
    left: 56px;
    top: 150px;
    display: flex;
    align-items: center;
    gap: 16px;
  }
  .brand__dot {
    width: 44px;
    height: 44px;
    border-radius: 50%;
    background: var(--purple);
    flex: none;
  }
  .brand__name {
    color: var(--purple);
    font-weight: 700;
    font-size: 36px;
    line-height: 1.02;
    text-transform: uppercase;
    letter-spacing: 0.5px;
  }

  .contact {
    position: absolute;
    right: 34px;
    top: 40px;
    text-align: right;
    color: var(--white);
  }
  .contact__name { font-weight: 700; font-size: 22px; line-height: 1.2; }
  .contact__role { font-size: 16px; margin-bottom: 28px; }
  .contact__address { font-size: 14px; line-height: 1.45; margin-bottom: 30px; }
  .contact__list { list-style: none; font-size: 14px; line-height: 1.6; }
  .contact__list li { display: flex; justify-content: flex-end; align-items: center; gap: 8px; }
  .icon { width: 13px; height: 13px; flex: none; }
</style>
</head>
<body>

<section class="card card--front" aria-label="Business card front">
  <svg class="card__shapes" viewBox="0 0 700 400" preserveAspectRatio="none" aria-hidden="true">
    <path fill="var(--green)" d="M140,0 C300,60 425,250 470,400 L700,400 L700,0 Z"/>
    <path fill="var(--white)" d="M176,0 C334,60 440,250 480,400 L700,400 L700,0 Z"/>
    <path fill="var(--purple)" d="M188,0 C346,60 448,250 486,400 L700,400 L700,0 Z"/>
  </svg>

  <div class="brand">
    <span class="brand__dot"></span>
    <p class="brand__name">Marlow's<br>Pet Care</p>
  </div>

  <div class="contact">
    <p class="contact__name">Daniel Okafor</p>
    <p class="contact__role">Director</p>
    <p class="contact__address">214, 6th floor, Arbor House<br>Kestrel Road WLD</p>
    <ul class="contact__list">
      <li>012 555 0148
        <svg class="icon" viewBox="0 0 16 16" aria-hidden="true"><rect x="4" y="1" width="8" height="14" rx="1.5" fill="none" stroke="#fff" stroke-width="1.5"/><circle cx="8" cy="12.5" r="0.9" fill="#fff"/></svg>
      </li>
      <li>012 555 0148
        <svg class="icon" viewBox="0 0 16 16" aria-hidden="true"><path fill="#fff" d="M3.5 1.5l2.5 0 1 3.5-1.6 1.2c.8 1.8 2.2 3.2 4 4l1.2-1.6 3.5 1v2.5c0 .8-.7 1.4-1.5 1.4C6.8 13.5 2.1 8.9 2.1 3c0-.8.6-1.5 1.4-1.5z"/></svg>
      </li>
      <li>hello@marlowspet.com
        <svg class="icon" viewBox="0 0 16 16" aria-hidden="true"><rect x="1" y="3" width="14" height="10" rx="1" fill="none" stroke="#fff" stroke-width="1.5"/><path d="M1.5 3.8L8 9l6.5-5.2" fill="none" stroke="#fff" stroke-width="1.5"/></svg>
      </li>
      <li>www.marlowspetcare.com
        <svg class="icon" viewBox="0 0 16 16" aria-hidden="true"><g fill="none" stroke="#fff" stroke-width="1.3"><circle cx="8" cy="8" r="6.5"/><ellipse cx="8" cy="8" rx="2.8" ry="6.5"/><path d="M1.5 8h13M2.5 4.8h11M2.5 11.2h11"/></g></svg>
      </li>
    </ul>
  </div>
</section>

<section class="card card--back" aria-label="Business card back"></section>

</body>
</html>
```